Fun, Clean Business Card For Family Focused Travel Agency

I need a business card using specific colors and fonts as in the uploaded files. Ideally, I would like a large image of the logo on the back and all the contact info on the front. Maybe the stars/dots somewhere in a flowy form.

I do want it the contact information to be clear and easy to read. I don't want it to look too busy. Maybe even a bit minimalist.

I plan or ordering the ROUNDED CORNER business cards from Cardwell Press, so please consider that in your design.

Target Market(s)

Families with children, couples, groups of friends

Contact Information for Business Card

Marla Quent, Owner
Marla@TidewayTrips.example
Cell Phone Number 555-218-6034
Office Phone Number 555-647-1295
Specializing in Fablecrest destinations, Goldmere Parkside Resort, Cruises and All-Inclusive Vacations.

Nice but not required:
www.TidewayTrips.example
Facebook, Instagram, Twitter icons with username: TidewayTrips

Font styles to use
Sans Serif

Requirements
Must have
• Please try to use the colors from the logo as much as possible. I understand lighter shades/colors may be needed for some things.
Should not have
• NO SERIF FONTS. That is really the only thing I do not want at all

```html
<!DOCTYPE html>
<html lang="en">
<head>
<meta charset="utf-8">
<title>Tideway Trips – Business Card</title>
<link href="https://fonts.googleapis.com/css2?family=Courgette&family=Ubuntu:wght@400;500;700&display=swap" rel="stylesheet">
<style>
  :root {
    --page-bg: #d9d4cc;
    --card-light-top: #f4f3f0;
    --card-light-bottom: #cfd6da;
    --panel-dark: #16171c;
    --panel-dark-2: #2a2b32;
    --brand-green: #1f8a63;
    --accent-green: #2fa57a;
    --text-light: #ececec;
    --text-muted: #c8a9a6;
    --ink: #1b1b1d;
  }
  * { margin: 0; padding: 0; box-sizing: border-box; }
  html, body { width: 1200px; height: 970px; overflow: hidden; }
  body {
    background: var(--page-bg);
    font-family: "Ubuntu", sans-serif;
    position: relative;
  }
  .card {
    position: absolute;
    left: 100px; top: 199px;
    width: 1000px; height: 572px;
    border-radius: 18px;
    overflow: hidden;
    background: linear-gradient(160deg, var(--card-light-top), var(--card-light-bottom));
    box-shadow: 0 12px 30px rgba(0,0,0,.25);
  }
  .card-shape { position: absolute; inset: 0; width: 100%; height: 100%; }
  .edge-tab {
    position: absolute; left: -16px; top: 84px;
    width: 36px; height: 56px; border-radius: 50%;
    background: var(--brand-green);
  }
  .holder-name {
    position: absolute; left: 56px; top: 78px;
    font-family: "Courgette", cursive;
    font-size: 44px; color: var(--text-light); line-height: 1;
  }
  .holder-role {
    position: absolute; left: 56px; top: 138px;
    font-size: 22px; color: var(--accent-green);
  }
  .contact-list {
    position: absolute; left: 56px; top: 236px;
    list-style: none;
  }
  .contact-item {
    display: flex; align-items: center; gap: 12px;
    height: 34px;
    font-size: 22px; color: var(--text-light);
  }
  .contact-icon { width: 28px; height: 28px; flex: none; }
  .specialty {
    position: absolute; left: 56px; top: 412px;
    font-size: 23px; line-height: 32px; color: var(--text-light);
  }
  .specialty .lead { color: var(--accent-green); font-weight: 500; }
  .specialty .more { color: var(--text-muted); }
  .social {
    position: absolute; left: 56px; top: 494px;
    display: flex; align-items: center; gap: 10px;
  }
  .social-box { width: 36px; height: 36px; background: var(--brand-green); }
  .social-handle { margin-left: 14px; font-size: 22px; color: var(--text-muted); }
  .brand {
    position: absolute; left: 580px; top: 112px;
    display: flex; align-items: center; gap: 18px;
  }
  .brand-dot { width: 96px; height: 96px; border-radius: 50%; background: var(--brand-green); }
  .brand-name { font-size: 52px; font-weight: 700; color: var(--ink); }
</style>
</head>
<body>
  <section class="card" aria-label="Tideway Trips business card">
    <svg class="card-shape" viewBox="0 0 1000 572" preserveAspectRatio="none" aria-hidden="true">
      <defs>
        <linearGradient id="panelGradient" x1="0" y1="0" x2="1" y2="1">
          <stop offset="0" stop-color="#1d1e24"/>
          <stop offset="0.5" stop-color="#2a2b32"/>
          <stop offset="1" stop-color="#0c0c10"/>
        </linearGradient>
      </defs>
      <path d="M365,0 H412 C422,130 472,214 582,256 C722,304 905,330 1000,452 V572 H0 Z" fill="#1f8a63"/>
      <path d="M0,0 H372 C392,140 440,232 562,272 C702,318 882,334 1000,472 V572 H0 Z" fill="url(#panelGradient)"/>
    </svg>

    <div class="edge-tab"></div>
    <h1 class="holder-name">Marla Quent</h1>
    <p class="holder-role">Owner</p>

    <ul class="contact-list">
      <li class="contact-item">
        <svg class="contact-icon" viewBox="0 0 28 28" aria-hidden="true"><circle cx="14" cy="14" r="14" fill="#1f8a63"/><rect x="10" y="7" width="8" height="14" rx="1.5" fill="none" stroke="#fff" stroke-width="1.8"/></svg>
        555-218-6034
      </li>
      <li class="contact-item">
        <svg class="contact-icon" viewBox="0 0 28 28" aria-hidden="true"><circle cx="14" cy="14" r="14" fill="#1f8a63"/><path d="M7 12 Q14 6 21 12 L19 14 L17 12 H11 L9 14 Z" fill="#fff"/><rect x="9" y="14" width="10" height="6" rx="1" fill="#fff"/></svg>
        555-647-1295
      </li>
      <li class="contact-item">
        <svg class="contact-icon" viewBox="0 0 28 28" aria-hidden="true"><circle cx="14" cy="14" r="14" fill="#1f8a63"/><rect x="7" y="9" width="14" height="10" fill="#fff"/><path d="M7 9 L14 15 L21 9" fill="none" stroke="#1f8a63" stroke-width="1.5"/></svg>
        Marla@TidewayTrips.example
      </li>
      <li class="contact-item">
        <svg class="contact-icon" viewBox="0 0 28 28" aria-hidden="true"><circle cx="14" cy="14" r="14" fill="#1f8a63"/><g fill="none" stroke="#fff" stroke-width="1.4"><circle cx="14" cy="14" r="7"/><ellipse cx="14" cy="14" rx="3" ry="7"/><path d="M7 14 H21"/></g></svg>
        www.TidewayTrips.example
      </li>
    </ul>

    <p class="specialty">
      <span class="lead">Specializing in</span> Fablecrest destinations<br>
      <span class="more">Goldmere Parkside Resort | Cruises and All-Inclusive Vacations.</span>
    </p>

    <div class="social">
      <span class="social-box"></span>
      <span class="social-box"></span>
      <span class="social-box"></span>
      <span class="social-handle">TidewayTrips</span>
    </div>

    <div class="brand">
      <span class="brand-dot"></span>
      <span class="brand-name">Tideway Trips</span>
    </div>
  </section>
</body>
</html>
```